Short term Rentals Marketing agency needs Web design.

We Need a web design for our new company based in Calgary, AB. We are a International Luxury home sharing company (short term rental properties, Villas, Boutique Hotels, Bed & Breakfast, Realtors, Mortgage Brokers). We would like to see designs that look simple, modern and professional. Colors would be bold (red, black, white). The final design should communicate something welcoming, symbolize innovation, and growth. Our goal is to form partnerships with Real Estate, Property Management, Short term Rental Clients to make their lives easier and increase revenue. Vlto Harbor Co. offers a flexible and secure way to market our clients properties while maintaining client satisfaction and amazing customer service. We like how https://plumtrellisads.ca/ is interactive (when you scroll down, text gets larger). Other similar websites for Short Term Rentals is https://www.thekeyhavenfirm.com/, https://stayvorabnb.com/, https://www.nestquill.com/, https://www.roostfinch.com/about-us/, https://lodgewardens.com. We have attached our Logo.

Target Market(s)

short term rental properties, Villas, Boutique Hotels, Bed & Breakfast, Realtors, Mortgage Brokers, property owners

Industry/Entity Type

Real Estate

Coding

Coded - Design and coding required

Number of Pages Required

5+ page

Font styles to use
Sans Serif

Requirements
Must have
• Home Page, About Us page, How it works, Services, Contact us.

We like how https://plumtrellisads.ca/ is interactive (when you scroll down, text gets larger).

We have attached our Webcopy. We would like Call to Action Buttons where they're located in the copy and page.

Must have our Logo Colors.

Other similar websites for Short Term Rentals is https://www.thekeyhavenfirm.com/, https://stayvorabnb.com/, https://www.nestquill.com/, https://www.roostfinch.com/about-us/, https://lodgewardens.com.
Nice to have
• Catchy, Interactive Home page.

Should not have
• Should not be too cluttered

```html
<!DOCTYPE html>
<html lang="en">
<head>
<meta charset="utf-8">
<title>Vlto Harbor Co. — Home</title>
<link rel="stylesheet" href="https://fonts.googleapis.com/css2?family=Fenix&family=Josefin+Sans:wght@700&family=Lato:wght@400&family=Montserrat:wght@400;500&family=Roboto:wght@400&display=swap">
<style>
:root{
  --red:#e31b2d;
  --black:#000;
  --ink:#1a1a1a;
  --grey-text:#8a8a8a;
  --nav-text:#9a9a9a;
  --soft:#fafafa;
  --white:#fff;
}
*{margin:0;padding:0;box-sizing:border-box}
html,body{width:1200px;height:3450px;overflow:hidden;background:var(--white)}
body{position:relative;font-family:"Lato",sans-serif;color:var(--ink)}
.abs{position:absolute}
.backdrop{position:absolute;left:0;top:0}
/* top bar */
.top-bar{left:0;top:0;width:1200px;height:37px;background:var(--black);color:var(--white);font-family:"Montserrat",sans-serif;font-size:11px}
.top-bar .call{position:absolute;left:842px;top:12px}
.top-bar .phone-box{position:absolute;left:921px;top:7px;width:24px;height:24px;background:var(--red)}
.top-bar .number{position:absolute;left:963px;top:12px;font-weight:500}
/* header */
.site-header{left:0;top:37px;width:1200px;height:75px;background:var(--white)}
.brand{position:absolute;left:171px;top:22px;display:flex;align-items:center;gap:10px}
.brand-square{width:26px;height:26px;background:var(--red)}
.brand-name{font-family:"Montserrat",sans-serif;font-weight:500;font-size:22px;color:var(--ink)}
.main-nav{position:absolute;top:31px;font-family:"Roboto",sans-serif;font-size:12.5px;color:var(--nav-text)}
.main-nav.active{color:var(--red)}
.search{position:absolute;left:874px;top:23px;width:165px;height:30px;border:1px solid #e5e5e5;border-radius:15px;font-family:"Roboto",sans-serif;font-size:11px;color:#666;padding:8px 10px}
.search svg{position:absolute;right:10px;top:8px}
/* hero */
.hero-photo{left:0;top:112px;width:1200px;height:600px;background:linear-gradient(170deg,#8c8a80 0%,#6f6b5c 35%,#4e5a3a 70%,#3c4a2c 100%)}
.hero-title{left:0;top:262px;width:1200px;text-align:center;font-family:"Josefin Sans",sans-serif;font-weight:700;font-size:44px;line-height:49px;color:var(--white);text-transform:uppercase;text-shadow:0 2px 6px rgba(0,0,0,.35)}
.btn{background:var(--red);color:var(--white);font-family:"Montserrat",sans-serif;font-weight:500;font-size:13px;text-align:center;text-transform:uppercase}
.hero-btn{left:524px;top:435px;width:150px;height:43px;line-height:43px}
/* headings */
.mark{position:absolute;width:44px;height:38px;border-top:5px solid var(--red);border-left:5px solid var(--red)}
.section-title{font-family:"Fenix",serif;font-size:36px;line-height:36px;color:var(--ink)}
.body-copy{font-size:10.5px;line-height:18.7px;color:var(--grey-text)}
/* steps */
.intro{left:300px;top:830px;width:600px;text-align:center;font-size:12px;line-height:21px;color:#555}
.step{position:absolute;top:906px;width:270px;text-align:center}
.step .ring{width:76px;height:76px;margin:0 auto;border-radius:50%;border:2px solid #f8d4d7;background:#fff5f6;display:flex;align-items:center;justify-content:center}
.step h3{margin-top:26px;font-family:"Montserrat",sans-serif;font-weight:500;font-size:14px;color:var(--ink)}
.step p{margin-top:8px;font-size:10.5px;line-height:18.7px;color:var(--grey-text)}
/* photo blocks */
.photo{position:absolute}
.feature-title{font-family:"Fenix",serif;font-size:35px;line-height:34px;color:var(--ink)}
/* newsletter */
.subscribe{left:292px;top:3022px;width:616px;height:44px;border:1px solid var(--red);background:var(--white)}
.subscribe .field{position:absolute;left:12px;top:15px;font-family:"Montserrat",sans-serif;font-size:11px;color:#444}
.subscribe .btn{position:absolute;left:476px;top:3px;width:135px;height:36px;line-height:36px}
/* footer */
.foot-brand{left:0;top:3250px;width:1200px;display:flex;justify-content:center;align-items:center;gap:12px}
.foot-brand .brand-name{color:var(--white);font-size:26px}
.foot-nav{left:0;top:3320px;width:1200px;text-align:center;font-family:"Montserrat",sans-serif;font-size:11px;color:var(--white);word-spacing:2px}
.copyright{left:0;top:3406px;width:1200px;text-align:center;font-family:"Montserrat",sans-serif;font-size:9.5px;color:var(--white)}
</style>
</head>
<body>

<svg class="backdrop" width="1200" height="3450" viewBox="0 0 1200 3450" aria-hidden="true">
  <path d="M0,1560 C260,1470 560,1480 820,1540 S1100,1520 1200,1490 L1200,2860 C1000,2830 700,2850 400,2830 S100,2840 0,2850 Z" fill="#fafafa"/>
  <path d="M0,3170 C250,3080 520,3150 780,3160 S1100,3110 1200,3100 L1200,3450 L0,3450 Z" fill="#000"/>
</svg>

<div class="abs top-bar">
  <span class="call">Call Us Now</span>
  <span class="phone-box"><svg width="24" height="24" viewBox="0 0 24 24"><path d="M8 6c1 0 2 2.5 2 3s-1 1-1 1.5 2 3.5 3.5 4c.5 0 1-1 1.5-1s3 1 3 2-1 2.5-2.5 2.5C10 18 6 13 6 8c0-1 1-2 2-2z" fill="#fff"/></svg></span>
  <span class="number">555.014.2290</span>
</div>

<header class="abs site-header">
  <div class="brand"><span class="brand-square"></span><span class="brand-name">Vlto Harbor Co.</span></div>
  <span class="main-nav active" style="left:493px">Home</span>
  <span class="main-nav" style="left:549px">About Us</span>
  <span class="main-nav" style="left:625px">How It Works</span>
  <span class="main-nav" style="left:721px">Services</span>
  <span class="main-nav" style="left:789px">Contact Us</span>
  <div class="search">Search here....
    <svg width="13" height="13" viewBox="0 0 13 13"><circle cx="5.5" cy="5.5" r="4" fill="none" stroke="#e31b2d" stroke-width="1.4"/><line x1="8.5" y1="8.5" x2="12" y2="12" stroke="#e31b2d" stroke-width="1.4"/></svg>
  </div>
</header>

<div class="abs hero-photo" role="img" aria-label="Photo of a couple and an agent in front of a brick house with a green garden"></div>
<svg class="abs" style="left:0;top:600px" width="1200" height="112" viewBox="0 0 1200 112" aria-hidden="true">
  <path d="M0,40 C150,110 320,120 560,72 S1000,0 1200,12 L1200,112 L0,112 Z" fill="#fff"/>
</svg>
<h1 class="abs hero-title">Partner with us<br>and let’s startgrowing<br>together!</h1>
<div class="abs btn hero-btn">Work with us</div>

<!-- How it works -->
<span class="mark" style="left:487px;top:757px"></span>
<h2 class="abs section-title" style="left:0;top:772px;width:1200px;text-align:center">How it woks</h2>
<p class="abs intro">We try to keep our application, management, and marketing process as quick and simple as possible. To sign up to Vlto Harbor Co, you can follow these three steps</p>

<div class="step" style="left:160px">
  <div class="ring"><svg width="34" height="34" viewBox="0 0 34 34" fill="none" stroke="#e31b2d" stroke-width="1.6"><rect x="9" y="5" width="18" height="24" rx="2"/><line x1="6" y1="10" x2="11" y2="10"/><line x1="6" y1="17" x2="11" y2="17"/><line x1="6" y1="24" x2="11" y2="24"/><path d="M15 12c1-1 3 0 3 2l-1 2 3 3 2-1c2 0 3 2 2 3"/></svg></div>
  <h3>Book A Consultation</h3>
  <p>Give us a call to set up your own consultation<br>session where we will discuss your needs, goals,<br>and concerns regarding the management and marketing<br>of your short-term rental properties.</p>
</div>
<div class="step" style="left:465px">
  <div class="ring"><svg width="34" height="34" viewBox="0 0 34 34" fill="none" stroke="#e31b2d" stroke-width="1.6"><path d="M11 15 L17 9 L23 15 V21 H11 Z"/><rect x="15" y="16" width="4" height="5"/><path d="M5 24 C9 22 12 23 15 25 H22 C24 25 24 27 22 27 H15"/><path d="M22 25 L28 22"/></svg></div>
  <h3>Optimize Your Property</h3>
  <p>Once you’ve decided what you would like from<br>your rental property, we will help you make it a<br>reality. This involves optimizing your pricing, listings,<br>operations, bookings, and much more.</p>
</div>
<div class="step" style="left:769px">
  <div class="ring"><svg width="34" height="34" viewBox="0 0 34 34" fill="none" stroke="#e31b2d" stroke-width="1.6"><rect x="7" y="6" width="16" height="22" rx="2"/><line x1="11" y1="12" x2="19" y2="12"/><line x1="11" y1="16" x2="17" y2="16"/><path d="M20 22 L25 17 L30 22 V28 H20 Z"/></svg></div>
  <h3>Start Hosting Renters</h3>
  <p>You can start hosting renters in no time thanks<br>to our quick turnaround times and professional<br>services. We will help you maintain your<br>properties for as long as you need us.</p>
</div>

<!-- Welcome -->
<span class="mark" style="left:161px;top:1177px"></span>
<h2 class="abs section-title" style="left:177px;top:1192px">Welcome To Vlto<br>Harbor Co.</h2>
<div class="abs body-copy" style="left:177px;top:1287px;width:430px">
  <p>Vlto Harbor Co. is here to manage and market your short-term rental properties so you don’t have to. Enjoy peace of mind in knowing your short-term rental properties, vacation homes, villas, hotels, and B&amp;Bs are safe, secure, and profitable - no matter where you are in the world. We will help you market, manage, and capitalize on everything, from your newest bookings to house cleaning and upkeep.</p>
  <p style="margin-top:9px">Vlto Harbor Co. saves you time, money, and effort, so that you can focus on the things that matter most to you.</p>
</div>
<div class="abs btn" style="left:177px;top:1454px;width:127px;height:46px;line-height:78px;overflow:hidden">Learn more</div>

<svg class="abs" style="left:644px;top:1192px" width="396" height="353" viewBox="0 0 396 353" aria-hidden="true">
  <polygon points="246,0 396,0 396,150 376,135 376,20 262,20" fill="#e31b2d"/>
  <polygon points="0,203 20,218 20,333 134,333 150,353 0,353" fill="#e31b2d"/>
</svg>
<div class="photo" role="img" aria-label="Photo of a modern white two-storey villa with lawn under blue sky" style="left:671px;top:1204px;width:360px;height:313px;background:linear-gradient(180deg,#6fa7d8 0%,#c9dbe8 45%,#d8d8d4 60%,#6b8d3a 100%)"></div>

<!-- Why choose us -->
<span class="mark" style="left:161px;top:1657px"></span>
<h2 class="abs section-title" style="left:177px;top:1672px">Why Choose Us</h2>

<svg class="abs" style="left:161px;top:1747px" width="396" height="300" viewBox="0 0 396 300" aria-hidden="true">
  <polygon points="246,0 396,0 396,150 376,135 376,20 262,20" fill="#e31b2d"/>
  <polygon points="0,150 20,165 20,280 134,280 150,300 0,300" fill="#e31b2d"/>
</svg>
<div class="photo" role="img" aria-label="Photo of three men shaking hands over a contract at a white table" style="left:187px;top:1758px;width:361px;height:262px;background:linear-gradient(160deg,#d9d2c6 0%,#b8a996 40%,#e8e6e2 75%,#f2f2f0 100%)"></div>
<h3 class="abs feature-title" style="left:644px;top:1745px">Optimize Your Property</h3>
<div class="abs body-copy" style="left:644px;top:1806px;width:395px">
  <p>Having Vlto Harbor Co. manage and market your rental property lets you benefit from increased revenues without having to put in the hours of work yourself. Vlto Harbor Co. will manage your property listings, advertise your listings, optimize your rental pricing, increase your occupancy, and help you offer the very best customer experience.</p>
  <p style="margin-top:18px">We won’t charge you a fixed monthly retainer! Instead, we work on a commissi-on-based system to give you a great hands-off opportunity. We charge 30% of the gross revenue your unit brings in per month. For example, if we’ve made $1,000,000 in a month on your property, you’ll take home $700,000 and we’ll only take $300,000!</p>
</div>

<h3 class="abs feature-title" style="left:163px;top:2181px">Receive Constant<br>Support</h3>
<p class="abs body-copy" style="left:163px;top:2280px;width:400px">Our dedicated team is there to take care of your property so that you don’t have to. Our affordable and professional services include being there to support your guests, constant technical communication, and on-site operations management.</p>
<svg class="abs" style="left:644px;top:2108px" width="396" height="300" viewBox="0 0 396 300" aria-hidden="true">
  <polygon points="246,0 396,0 396,150 376,135 376,20 262,20" fill="#e31b2d"/>
  <polygon points="0,150 20,165 20,280 134,280 150,300 0,300" fill="#e31b2d"/>
</svg>
<div class="photo" role="img" aria-label="Photo of three smiling colleagues looking at a tablet in a warmly lit cafe" style="left:671px;top:2118px;width:360px;height:262px;background:linear-gradient(160deg,#3a2a1c 0%,#7a5532 40%,#b98a5a 65%,#4a4036 100%)"></div>

<svg class="abs" style="left:161px;top:2466px" width="396" height="300" viewBox="0 0 396 300" aria-hidden="true">
  <polygon points="246,0 396,0 396,150 376,135 376,20 262,20" fill="#e31b2d"/>
  <polygon points="0,150 20,165 20,280 134,280 150,300 0,300" fill="#e31b2d"/>
</svg>
<div class="photo" role="img" aria-label="Photo of hands holding a tablet over financial documents" style="left:187px;top:2478px;width:361px;height:262px;background:linear-gradient(135deg,#e9dcc2 0%,#b7ad9c 35%,#5b5c60 65%,#2f3136 100%)"></div>
<h3 class="abs feature-title" style="left:644px;top:2550px">Manage Your Risks and<br>Insurance</h3>
<p class="abs body-copy" style="left:644px;top:2646px;width:395px">Vlto Harbor Co. will help you protect your property income by giving you the security and insurance you need when it comes to pricing and managing your security deposits. Please note that terms and conditions apply.</p>

<!-- Newsletter -->
<span class="mark" style="left:435px;top:2872px"></span>
<h2 class="abs section-title" style="left:0;top:2887px;width:1220px;text-align:center">Subcribe Newsletter</h2>
<p class="abs" style="left:300px;top:2952px;width:600px;text-align:center;font-size:12px;line-height:21px;color:#555">Lorem ipsum dolor sit amet, consectetur adipiscing elit, sed do eiusmod tempor incididunt ut labore et dolore magna aliqua. Ut enim ad minim veniam, quis nostrud exercitation .</p>
<div class="abs subscribe">
  <span class="field">Enter Email</span>
  <span class="btn" style="top:3px">Subscribe</span>
</div>

<!-- Footer -->
<div class="abs foot-brand"><span class="brand-square"></span><span class="brand-name">Vlto Harbor Co.</span></div>
<nav class="abs foot-nav">Home &nbsp;|&nbsp; About Us &nbsp;|&nbsp; How it works &nbsp;|&nbsp; Our services &nbsp;|&nbsp; Contact Us</nav>
<p class="abs copyright">Copyright © Vlto Harbor Co - 2020 . All Right reserved.</p>

</body>
</html>
```